The Harbourline Aid Trust needs a graphic of their innovation approach

What we need?
- we have designed a new innovation approach (see attached). An innovation approach is the process one goes through in order to design and launch a new product or service.
- This new graphic will be used in meetings to help others understand what innovation is and how we do it. It will also be used in training sessions and be the starting point for innovation training materials we are creating
- We have created this draft graphic by copying and pasting new words over another charities innovation process
- We would like you to use your design magic and create our very own innovation process graphic. We would like it to be neat, simple, non fussy, easy to understand /read and in line with our brand colours
Attached:
1. PowerPoint:
- Slide 1: our innovation process
- Slide 2 explanation of process to bring it to life
- Slide 3&4: brand colours
- Slide 5: inspiration / examples of other processes we like the look of
2. Typeface brand guidelines
We can't wait to see what you come up with! Thank you :)
internal employees
Charity

```html
<!DOCTYPE html>
<html lang="en">
<head>
<meta charset="utf-8">
<title>Innovation Approach</title>
<link rel="stylesheet" href="https://fonts.googleapis.com/css2?family=Montserrat:wght@700;800&display=swap">
<style>
  :root {
    --discover-blue: #1689bd;
    --define-orange: #f0b03c;
    --deliver-red: #ee2b24;
    --ring-grey: #efefef;
    --marker-black: #000000;
    --label-ink: #111111;
    --paper: #ffffff;
  }
  html, body {
    margin: 0;
    padding: 0;
    width: 1200px;
    height: 800px;
    overflow: hidden;
    background: var(--paper);
  }
  .innovation-process {
    display: block;
    width: 1200px;
    height: 800px;
    font-family: "Montserrat", Arial, sans-serif;
  }
  .phase-ring { fill: var(--ring-grey); }
  .phase-gap { fill: var(--paper); }
  .band--discover { fill: var(--discover-blue); }
  .band--define { fill: var(--define-orange); }
  .band--deliver { fill: var(--deliver-red); }
  .phase-hub { filter: drop-shadow(0 3px 4px rgba(0,0,0,0.25)); }
  .phase-hub--discover { fill: var(--discover-blue); }
  .phase-hub--define { fill: var(--define-orange); }
  .phase-hub--deliver { fill: var(--deliver-red); }
  .phase-name {
    fill: var(--paper);
    font-size: 15px;
    font-weight: 700;
    text-anchor: middle;
    dominant-baseline: middle;
  }
  .milestone {
    fill: var(--marker-black);
    stroke: var(--paper);
    stroke-width: 4;
  }
  .leader {
    stroke: var(--label-ink);
    stroke-width: 2;
    stroke-dasharray: 7 6;
  }
  .milestone-label {
    fill: var(--label-ink);
    font-size: 16px;
    font-weight: 800;
    letter-spacing: 0.5px;
    text-anchor: middle;
  }
  .step-label {
    font-size: 21px;
    font-weight: 700;
    letter-spacing: 1px;
    text-anchor: middle;
  }
  .step-label--discover { fill: var(--discover-blue); }
  .step-label--define { fill: var(--define-orange); }
  .step-label--deliver { fill: var(--deliver-red); }
</style>
</head>
<body>
<svg class="innovation-process" viewBox="0 0 1200 800" role="img" aria-label="Innovation approach: Discover, Define, Deliver">
  <defs>
    <path id="discover-label-path" d="M231.3,445.9 A149 149 0 0 0 524.7,445.9"/>
    <path id="define-label-path" d="M451,396.7 A134 134 0 0 1 715,396.7"/>
    <path id="deliver-label-path" d="M664,494.5 A149 149 0 0 0 922,494.5"/>
  </defs>

  <!-- phase rings -->
  <circle class="phase-ring" cx="378" cy="420" r="126"/>
  <circle class="phase-ring" cx="583" cy="420" r="126"/>
  <circle class="phase-ring" cx="793" cy="420" r="126"/>
  <circle class="phase-gap" cx="378" cy="420" r="80"/>
  <circle class="phase-gap" cx="583" cy="420" r="80"/>
  <circle class="phase-gap" cx="793" cy="420" r="80"/>

  <!-- process track -->
  <rect class="band--discover" x="70" y="420" width="228" height="46"/>
  <path class="band--discover" d="M252,420 A126 126 0 0 0 504,420 L458,420 A80 80 0 0 1 298,420 Z"/>
  <path class="band--define" d="M457,420 A126 126 0 0 1 709,420 L663,420 A80 80 0 0 0 503,420 Z"/>
  <path class="band--deliver" d="M667,420 A126 126 0 0 0 919,420 L873,420 A80 80 0 0 1 713,420 Z"/>
  <rect class="band--deliver" x="873" y="420" width="220" height="46"/>
  <polygon class="band--deliver" points="1090,410 1146,443 1090,476"/>

  <!-- phase hubs -->
  <circle class="phase-hub phase-hub--discover" cx="380" cy="420" r="58"/>
  <text class="phase-name" x="380" y="421">DISCOVER</text>
  <circle class="phase-hub phase-hub--define" cx="583" cy="420" r="58"/>
  <text class="phase-name" x="583" y="421">DEFINE</text>
  <circle class="phase-hub phase-hub--deliver" cx="793" cy="420" r="58"/>
  <text class="phase-name" x="793" y="421">DELIVER</text>

  <!-- leaders -->
  <line class="leader" x1="165" y1="326" x2="165" y2="418"/>
  <line class="leader" x1="378" y1="552" x2="378" y2="645"/>
  <line class="leader" x1="585" y1="198" x2="585" y2="290"/>
  <line class="leader" x1="697" y1="470" x2="697" y2="650"/>
  <line class="leader" x1="955" y1="326" x2="955" y2="418"/>

  <!-- step labels -->
  <text class="step-label step-label--discover"><textPath href="#discover-label-path" startOffset="24%">INSIGHT</textPath></text>
  <text class="step-label step-label--discover"><textPath href="#discover-label-path" startOffset="70%">IDEATE</textPath></text>
  <text class="step-label step-label--define"><textPath href="#define-label-path" startOffset="27%">(IN)VALIDATE</textPath></text>
  <text class="step-label step-label--define"><textPath href="#define-label-path" startOffset="73%">TEST</textPath></text>
  <text class="step-label step-label--deliver"><textPath href="#deliver-label-path" startOffset="50%">DELIVERY PLAN</textPath></text>

  <!-- milestones -->
  <circle class="milestone" cx="165" cy="445" r="27"/>
  <circle class="milestone" cx="378" cy="525" r="27"/>
  <circle class="milestone" cx="585" cy="316" r="27"/>
  <circle class="milestone" cx="688" cy="443" r="27"/>
  <circle class="milestone" cx="955" cy="443" r="27"/>

  <!-- milestone labels -->
  <text class="milestone-label" x="164" y="317">CHALLENGE</text>
  <text class="milestone-label" x="582" y="189">CONCEPTS</text>
  <text class="milestone-label" x="951" y="317">LAUNCH</text>
  <text class="milestone-label" x="380" y="670">OPPORTUNITY</text>
  <text class="milestone-label" x="380" y="692">STATEMENT</text>
  <text class="milestone-label" x="704" y="674">SOLUTION</text>
</svg>
</body>
</html>
```